Brackens Winery label master

We are looking for a classic and vintage looking wine label. Focus is on updating the family coat of arms with both color and without color. Font to be legible but classic in nature. For the label we need be able to change out the varietal and vintage and location/AVA but for the first design project we would like to use the year/vintage 2016 and the varietal/type of wine : Pinot Noir and for the AVA it will say Central Coast.

Target Market(s)

Wine drinkers between ages 30-70

Industry/Entity Type

Winery

Logo Text

Tarrant

Font styles to use
Script

Requirements
Must have
• Tarrant Coat of Arms with vines on top and the motto. Label size must not be over 5.5 x 3"
Nice to have
• Classic natural color and off black color fonts
Should not have
• Anything eligible or hard to read. Classic and Elegant but not overly ornate

```html
<!DOCTYPE html>
<html lang="en">
<head>
<meta charset="utf-8">
<title>Tarrant Pinot Noir – Brackens Winery label</title>
<link rel="stylesheet" href="https://fonts.googleapis.com/css2?family=Dancing+Script:wght@500&family=Quattrocento:wght@400&display=swap">
<style>
  :root {
    --label-ground: #eaf0de;
    --frame-gold: #9c8d62;
    --ink-grey: #66686b;
    --motto-ink: #2f2f2f;
    --keyline: #6b6b6b;
    --page: #ffffff;
  }
  html, body {
    margin: 0;
    padding: 0;
    width: 720px;
    height: 1200px;
    overflow: hidden;
    background: var(--page);
  }
  .wine-label {
    display: block;
    width: 720px;
    height: 1200px;
  }
  .label-frame { fill: var(--frame-gold); }
  .label-field { fill: var(--label-ground); }
  .label-keyline { fill: none; stroke: var(--keyline); stroke-width: 2.5; }
  .crest-art { fill: url(#crestTone); }
  .motto {
    font-family: "Quattrocento", serif;
    font-size: 20px;
    letter-spacing: 1px;
    fill: var(--motto-ink);
  }
  .brand-name {
    font-family: "Dancing Script", cursive;
    font-weight: 500;
    font-size: 200px;
    fill: var(--ink-grey);
  }
  .varietal {
    font-family: "Quattrocento", serif;
    font-size: 74px;
    fill: var(--ink-grey);
  }
  .vintage {
    font-family: "Quattrocento", serif;
    font-size: 50px;
    letter-spacing: 3px;
    fill: var(--frame-gold);
  }
  .vintage-rule { stroke: var(--frame-gold); stroke-width: 2.5; fill: none; }
  .appellation {
    font-family: "Quattrocento", serif;
    font-size: 40px;
    letter-spacing: 1px;
    fill: var(--ink-grey);
  }
</style>
</head>
<body>
<svg class="wine-label" viewBox="0 0 900 1500" xmlns="http://www.w3.org/2000/svg">
  <defs>
    <path id="labelShape" d="M190,225 C190,90 310,12 450,12 C590,12 710,90 710,225 L838,225 L838,338 Q895,345 895,420 L895,1100 Q895,1172 838,1180 L838,1278 L710,1278 C710,1410 590,1492 450,1492 C310,1492 190,1410 190,1278 L62,1278 L62,1180 Q5,1172 5,1100 L5,420 Q5,345 62,338 L62,225 Z"/>
    <path id="mottoCurve" d="M340,780 Q450,820 560,780"/>
    <radialGradient id="crestTone" cx="50%" cy="50%" r="60%">
      <stop offset="0%" stop-color="#e4dfc4"/>
      <stop offset="70%" stop-color="#d6cca6"/>
      <stop offset="100%" stop-color="#eaf0de" stop-opacity="0"/>
    </radialGradient>
  </defs>

  <g class="label-body">
    <use href="#labelShape" class="label-frame"/>
    <use href="#labelShape" class="label-field" transform="translate(450 752) scale(0.972 0.983) translate(-450 -752)"/>
    <use href="#labelShape" class="label-keyline" transform="translate(450 752) scale(0.972 0.983) translate(-450 -752)"/>
  </g>

  <g class="crest">
    <rect class="crest-art" x="140" y="145" width="620" height="680" rx="60"
          role="img" aria-label="Family coat of arms: shield with a diagonal patterned band, knight's helmet crowned with vine sprigs, scrolling mantling and a motto ribbon"/>
    <text class="motto" text-anchor="middle">
      <textPath href="#mottoCurve" startOffset="50%">VIRTUS ET VITIS</textPath>
    </text>
  </g>

  <text class="brand-name" x="450" y="1040" text-anchor="middle">Tarrant</text>

  <text class="varietal" x="450" y="1172" text-anchor="middle">Pinot Noir</text>

  <g class="vintage-block">
    <line class="vintage-rule" x1="205" y1="1240" x2="365" y2="1240"/>
    <line class="vintage-rule" x1="255" y1="1228" x2="365" y2="1228"/>
    <line class="vintage-rule" x1="255" y1="1252" x2="365" y2="1252"/>
    <line class="vintage-rule" x1="535" y1="1240" x2="695" y2="1240"/>
    <line class="vintage-rule" x1="535" y1="1228" x2="645" y2="1228"/>
    <line class="vintage-rule" x1="535" y1="1252" x2="645" y2="1252"/>
    <line class="vintage-rule" x1="340" y1="1212" x2="560" y2="1212"/>
    <line class="vintage-rule" x1="340" y1="1270" x2="560" y2="1270"/>
    <line class="vintage-rule" x1="368" y1="1218" x2="368" y2="1264"/>
    <line class="vintage-rule" x1="532" y1="1218" x2="532" y2="1264"/>
    <text class="vintage" x="450" y="1260" text-anchor="middle">2016</text>
  </g>

  <text class="appellation" x="458" y="1364" text-anchor="middle">Central Coast</text>
</svg>
</body>
</html>
```